Update New Business Card - For Start Up

I need to update my business card, I have our old version for example. I would like to keep to the same colors and theme. We are a threat reporting and case management tool for corporations and educational institutions.

Target Market(s)

Corporate Security and Human Resources, School Administrators and Superintendents.

Industry/Entity Type

Physical Security and Technology.

Contact Information for Business Card

My Name, Founder/CEO, phone number 777-412-5068, Logo, Web...

Colors
0054AA
0677BA
7BADD7
CADEEF
E8F1F8

Requirements
Must have
• Something new and trendy.

```html
<!DOCTYPE html>
<html lang="en">
<head>
<meta charset="utf-8">
<title>Veltrace Business Card</title>
<link rel="stylesheet" href="https://fonts.googleapis.com/css2?family=Poppins:wght@400;500;600;700&display=swap">
<style>
  :root {
    --stage: #c8c8c8;
    --navy: #021a45;
    --blue-mid: #0a4f9c;
    --blue-bright: #1570c8;
    --brand-blue: #1e6fc0;
    --icon-ring: #3a8ee0;
    --white: #ffffff;
    --ink: #111111;
    --ink-soft: #555555;
    --ink-contact: #444444;
    --trace-light: #e3e6ea;
  }
  * { margin: 0; padding: 0; box-sizing: border-box; }
  html, body { width: 1200px; height: 1000px; overflow: hidden; }
  body {
    background: var(--stage);
    font-family: "Poppins", sans-serif;
    position: relative;
  }
  .card { position: absolute; overflow: hidden; }
  .card-front {
    left: 95px; top: 108px; width: 620px; height: 372px;
    background: linear-gradient(90deg, var(--navy) 0%, var(--blue-mid) 45%, var(--blue-bright) 100%);
  }
  .card-back {
    left: 477px; top: 511px; width: 623px; height: 373px;
    background: var(--white);
  }
  .circuit-area { position: absolute; }
  .card-front .circuit-area {
    right: 0; top: 0; width: 320px; height: 200px;
    background: radial-gradient(ellipse at 100% 0%, rgba(10,40,90,0.45) 0%, rgba(10,40,90,0) 70%);
  }
  .card-back .circuit-area {
    right: 0; top: 0; width: 320px; height: 180px;
    background: radial-gradient(ellipse at 100% 0%, var(--trace-light) 0%, rgba(255,255,255,0) 70%);
  }
  .brand { position: absolute; display: flex; align-items: center; }
  .brand-dot { border-radius: 50%; flex-shrink: 0; }
  .brand-name { font-weight: 500; text-transform: uppercase; line-height: 1; }
  .card-front .brand { left: 156px; top: 154px; gap: 10px; }
  .card-front .brand-dot { width: 64px; height: 64px; background: var(--white); }
  .card-front .brand-name { color: var(--white); font-size: 30px; letter-spacing: 4px; }
  .card-back .brand { left: 35px; top: 42px; gap: 6px; }
  .card-back .brand-dot { width: 43px; height: 43px; background: var(--brand-blue); }
  .card-back .brand-name { color: var(--brand-blue); font-size: 20px; letter-spacing: 2.5px; }
  .holder { position: absolute; left: 0; right: 0; top: 148px; text-align: center; padding-left: behavior; }
  .holder-name { font-size: 37px; font-weight: 700; color: var(--ink); line-height: 1.1; padding-left: 0; margin-left: 0; transform: translateX(0); }
  .holder-title { font-size: 20px; font-weight: 600; color: var(--ink-soft); line-height: 1.2; }
  .contacts { position: absolute; left: 0; right: 0; top: 258px; }
  .contact { position: absolute; width: 200px; text-align: center; transform: translateX(-50%); }
  .contact-icon {
    width: 50px; height: 50px; margin: 0 auto 18px;
    border: 2px solid var(--icon-ring); border-radius: 50%;
    display: flex; align-items: center; justify-content: center;
  }
  .contact-text { font-size: 17px; font-weight: 500; color: var(--ink-contact); }
</style>
</head>
<body>
  <section class="card card-front">
    <div class="circuit-area" role="img" aria-label="Circuit board trace pattern"></div>
    <div class="brand">
      <span class="brand-dot"></span>
      <span class="brand-name">Veltrace</span>
    </div>
  </section>

  <section class="card card-back">
    <div class="circuit-area" role="img" aria-label="Light grey circuit board trace pattern"></div>
    <div class="brand">
      <span class="brand-dot"></span>
      <span class="brand-name">Veltrace</span>
    </div>
    <div class="holder" style="left:20px">
      <h1 class="holder-name">Owen Marlow</h1>
      <p class="holder-title">Founder/CEO</p>
    </div>
    <div class="contacts">
      <div class="contact" style="left:130px">
        <div class="contact-icon">
          <svg width="24" height="24" viewBox="0 0 24 24" fill="none" stroke="#333" stroke-width="2" stroke-linecap="round">
            <path d="M4 14v-2a8 8 0 0 1 16 0v2"/>
            <rect x="3" y="13" width="4" height="6" rx="1.5" fill="#333"/>
            <rect x="17" y="13" width="4" height="6" rx="1.5" fill="#333"/>
            <path d="M19 19c0 2-2 3-5 3"/>
          </svg>
        </div>
        <p class="contact-text">777-412-5068</p>
      </div>
      <div class="contact" style="left:310px">
        <div class="contact-icon">
          <svg width="24" height="24" viewBox="0 0 24 24">
            <rect x="2" y="5" width="20" height="14" rx="1.5" fill="#333"/>
            <path d="M2.5 6l9.5 7 9.5-7" fill="none" stroke="#fff" stroke-width="1.6"/>
          </svg>
        </div>
        <p class="contact-text">info@veltrace.co</p>
      </div>
      <div class="contact" style="left:493px">
        <div class="contact-icon">
          <svg width="22" height="22" viewBox="0 0 24 24" fill="none" stroke="#333" stroke-width="1.8">
            <circle cx="12" cy="12" r="9"/>
            <ellipse cx="12" cy="12" rx="4" ry="9"/>
            <path d="M3 12h18M5 7h14M5 17h14"/>
          </svg>
        </div>
        <p class="contact-text">www.veltrace.co</p>
      </div>
    </div>
  </section>
</body>
</html>
```